Fernwick Digital Marketing Agency Website Design. I need a new website for my digital marketing agency. It needs to be FAST and easy to use. I want to be able to add videos to the main homepage like this page: https://www.lumatreeweb.example/search-marketing/cleveland-ohio-seo-companyI'd like to have the request quote tab on the top right side as well as my number above it. The following website is my favorite overall: http://www.vantorelgroup.example/ I'd love to copy something like that.

***** Website I want to copy: http://www.vantorelgroup.example/services/ ******
Updates

This needs to be a Wordpress website. Sorry for any confusion as this is the first time using MakerQuill. I need the homepage as described as well as a Services Page and Contact Us page. Services page should be simply yet creative with a spot for me to insert up to 8 services.

Target Market(s)

Business owners

Industry/Entity Type

Digital Marketing

Coding

Coded - Design and coding required

Number of Pages Required

3 page

Font styles to use
Other font styles liked:
• Oswald

Colors

Designer to choose colors to be used in the design.

Requirements
Must have
• I need to have a nice design/template to work off of in Wordpress. It needs to be bright and vibrant yet elegant in design.
Nice to have
• CTA at the top right as well as a place for the phone number. http://www.vantorelgroup.example/services/

```html
<!DOCTYPE html>
<html lang="en">
<head>
<meta charset="utf-8">
<title>Fernwick Digital Marketing Agency</title>
<link rel="stylesheet" href="https://fonts.googleapis.com/css2?family=Oswald:wght@300;400;500;700&display=swap">
<style>
:root{
  --blue:#3e62a8;
  --blue-deep:#474d8c;
  --orange:#ff6a00;
  --ink:#222;
  --text:#555;
  --ghost:#f3f3f5;
  --white:#fff;
}
*{box-sizing:border-box;margin:0;padding:0}
html,body{width:1200px;height:2503px;overflow:hidden;background:var(--white)}
body{position:relative;font-family:'Oswald',sans-serif;color:var(--ink)}
.abs{position:absolute}
.btn{position:absolute;display:flex;align-items:center;justify-content:center;background:var(--orange);color:var(--white);font-weight:500;font-size:14px;text-transform:uppercase;border-radius:2px;box-shadow:0 3px 6px rgba(0,0,0,.15);text-decoration:none}
/* hero */
.hero{position:absolute;left:0;top:0;width:1200px;height:513px}
.hero svg{position:absolute;left:0;top:0}
.brand{position:absolute;left:130px;top:36px;display:flex;align-items:center;gap:12px;color:var(--white);font-weight:700;font-size:19px;letter-spacing:.5px}
.brand-dot{width:30px;height:30px;border-radius:50%;background:var(--white)}
.nav{position:absolute;top:41px;display:flex;color:var(--white);font-size:11px;text-transform:uppercase}
.nav span{position:absolute;white-space:nowrap}
.hero-kicker{position:absolute;left:127px;top:175px;color:var(--white);font-weight:300;font-size:28px;letter-spacing:3px}
.hero-title{position:absolute;left:127px;top:210px;color:var(--white);font-weight:700;font-size:60px;line-height:62px;text-transform:uppercase}
/* steps */
.section-title{position:absolute;left:0;width:1200px;text-align:center}
.ghost{top:610px;font-size:84px;font-weight:700;color:var(--ghost);letter-spacing:2px}
.heading{top:595px;font-size:24px;font-weight:700;color:var(--ink)}
.rule{position:absolute;left:582px;width:36px;height:2px;background:var(--ink)}
.panel{position:absolute;width:487px;height:325px;background:linear-gradient(135deg,var(--blue),var(--blue-deep))}
.card{position:absolute;width:348px;height:248px;background:var(--white);box-shadow:0 2px 10px rgba(0,0,0,.12);display:flex;flex-direction:column;align-items:center;justify-content:center;text-align:center;padding:0 40px;color:var(--text);font-weight:300;font-size:12.5px;line-height:21px}
.card p+p{margin-top:12px}
.step-label{position:absolute;color:var(--white);font-weight:300;font-size:21px;letter-spacing:2px;text-transform:uppercase}
.step-title{position:absolute;color:var(--white);font-weight:700;font-size:45px;line-height:44px;text-transform:uppercase}
.right{text-align:right}
.avatar{width:50px;height:50px;border-radius:50%;background:#8a8f99;margin-bottom:18px}
.quote{color:var(--blue);font-size:30px;font-weight:700;line-height:20px;margin-top:14px;height:20px}
.ticks{display:flex;gap:38px;margin-top:26px;color:var(--ink);font-weight:400;font-size:13px}
.ticks span{display:flex;align-items:center;gap:10px}
/* contact */
.contact{position:absolute;left:0;top:1860px;width:1200px;height:643px}
.contact svg{position:absolute;left:0;top:0}
.contact-title{top:2000px;color:var(--white);font-size:24px;font-weight:700}
.label{position:absolute;color:var(--white);font-size:12px;font-weight:500}
.field{position:absolute;background:var(--white);border-radius:3px}
.send{position:absolute;left:791px;top:2308px;width:119px;height:29px;border:1px solid rgba(255,255,255,.8);border-radius:3px;color:var(--white);font-size:11px;font-weight:500;display:flex;align-items:center;justify-content:center;text-transform:uppercase}
.info{position:absolute;top:2396px;color:var(--white);font-size:12px}
.foot-links{position:absolute;top:2443px;color:var(--white);font-size:9px;text-transform:uppercase}
.foot-links span{position:absolute;white-space:nowrap}
.copyright{position:absolute;top:2474px;left:0;width:1200px;text-align:center;color:var(--white);font-size:8px}
.social{position:absolute;top:2473px;width:14px;height:14px;border:1.5px solid var(--white);border-radius:50%}
</style>
</head>
<body>

<header class="hero">
  <svg width="1200" height="513" role="img" aria-label="Photo of a team working at laptops with a rocket line illustration, tinted blue">
    <defs>
      <linearGradient id="heroTint" x1="0" y1="0" x2="1" y2="1">
        <stop offset="0" stop-color="#3f64ab"/>
        <stop offset="1" stop-color="#45508f"/>
      </linearGradient>
    </defs>
    <polygon points="0,0 1152,0 923,513 0,513" fill="url(#heroTint)"/>
  </svg>
  <div class="brand"><span class="brand-dot"></span>FERNWICK</div>
  <nav class="nav">
    <span style="left:631px">Our Services</span>
    <span style="left:739px">Subscribe</span>
    <span style="left:828px">Testimonials</span>
  </nav>
  <a class="btn" style="left:940px;top:35px;width:113px;height:32px;font-size:11px">Get in touch</a>
  <div class="hero-kicker">DIGITAL MARKETING</div>
  <h1 class="hero-title">Search<br>Optimization</h1>
  <a class="btn" style="left:130px;top:370px;width:149px;height:37px">Get in touch</a>
</header>

<main>
  <div class="section-title ghost">WHAT YOU GET</div>
  <h2 class="section-title heading">WHAT YOU GET</h2>
  <div class="rule" style="top:640px"></div>

  <!-- step one -->
  <div class="panel" style="left:471px;top:689px"></div>
  <div class="card" style="left:284px;top:728px;height:247px">
    <p>When planning a corporate event, you don't want to schedule something that is going to be a negative in the eyes of your team. Team building exercises are only successful when everyone involved is excited.</p>
    <p>When planning a corporate event, you don't want to schedule something that is going to be a negative in</p>
  </div>
  <div class="step-label" style="left:659px;top:765px">First step</div>
  <div class="step-title" style="left:659px;top:792px">Consultation<br>with team</div>
  <a class="btn" style="left:633px;top:911px;width:167px;height:37px">Get in touch</a>

  <!-- step two -->
  <div class="panel" style="left:200px;top:1058px"></div>
  <div class="card" style="left:516px;top:1097px">
    <div class="avatar" role="img" aria-label="Client portrait"></div>
    <p>When planning a corporate event, you don't want to schedule something that is going to be a negative in the eyes of your team. Team building exercises are only successful when everyone involved is excited.</p>
    <div class="quote">&#8221;</div>
  </div>
  <div class="step-label right" style="left:200px;width:290px;top:1139px">Second step</div>
  <div class="step-title right" style="left:200px;width:290px;top:1166px">Creating<br>a plan</div>
  <a class="btn" style="left:352px;top:1283px;width:164px;height:37px;justify-content:flex-start;padding-left:18px">Get in touch</a>

  <!-- faint decoration -->
  <svg class="abs" style="left:880px;top:1560px" width="320" height="360" role="img" aria-label="Faint rocket line illustration">
    <ellipse cx="200" cy="180" rx="170" ry="190" fill="#eef0f6" opacity=".6"/>
  </svg>

  <!-- step three -->
  <div class="panel" style="left:471px;top:1422px"></div>
  <div class="card" style="left:284px;top:1460px;height:249px">
    <p>When planning a corporate event, you don't want to schedule something that is going to be a negative in the eyes of your team. Team building exercises are only successful when everyone involved is excited.</p>
    <div class="ticks">
      <span><svg width="20" height="16" viewBox="0 0 20 16"><path d="M2 8l6 6L18 2" fill="none" stroke="#ff6a00" stroke-width="3"/></svg>Increased Value</span>
      <span><svg width="20" height="16" viewBox="0 0 20 16"><path d="M2 8l6 6L18 2" fill="none" stroke="#ff6a00" stroke-width="3"/></svg>Time Saved</span>
    </div>
  </div>
  <div class="step-label" style="left:652px;top:1513px">Third step</div>
  <div class="step-title" style="left:652px;top:1540px">Confirm &amp;<br>start a plan</div>
  <a class="btn" style="left:633px;top:1649px;width:167px;height:37px">Get in touch</a>
</main>

<footer>
  <div class="contact">
    <svg width="1200" height="643" role="img" aria-label="Photo of a team meeting in an office, tinted blue">
      <defs>
        <linearGradient id="footTint" x1="0" y1="0" x2="1" y2="1">
          <stop offset="0" stop-color="#3f64ab"/>
          <stop offset="1" stop-color="#44518f"/>
        </linearGradient>
      </defs>
      <path d="M0 22 C250 10 520 65 760 62 C960 60 1100 42 1200 32 L1200 643 L0 643 Z" fill="url(#footTint)"/>
    </svg>
  </div>
  <h2 class="section-title contact-title">GET IN TOUCH!</h2>
  <div class="rule" style="top:2042px;background:var(--white)"></div>

  <div class="label" style="left:299px;top:2071px">Name</div>
  <div class="label" style="left:616px;top:2071px">Email Address</div>
  <div class="field" style="left:299px;top:2095px;width:299px;height:35px"></div>
  <div class="field" style="left:616px;top:2095px;width:294px;height:35px"></div>
  <div class="label" style="left:299px;top:2141px">Your Message</div>
  <div class="field" style="left:299px;top:2166px;width:611px;height:121px"></div>
  <div class="send">Send message</div>

  <div class="info" style="right:681px">hello@fernwick.example</div>
  <svg class="abs" style="left:536px;top:2400px" width="13" height="10" viewBox="0 0 13 10"><rect width="13" height="10" rx="1" fill="#fff"/><path d="M0 1l6.5 5L13 1" fill="none" stroke="#4a5a9c" stroke-width="1.2"/></svg>
  <div class="info" style="left:578px;top:2393px;font-size:17px;font-weight:700">FERNWICK</div>
  <svg class="abs" style="left:652px;top:2399px" width="11" height="11" viewBox="0 0 24 24"><path d="M6.6 10.8a15 15 0 006.6 6.6l2.2-2.2c.3-.3.7-.4 1-.2 1.1.4 2.3.6 3.6.6.6 0 1 .4 1 1V20c0 .6-.4 1-1 1A17 17 0 013 4c0-.6.4-1 1-1h3.5c.6 0 1 .4 1 1 0 1.3.2 2.5.6 3.6.1.3 0 .7-.2 1z" fill="#fff"/></svg>
  <div class="info" style="left:672px">+370 600 123 45</div>

  <div class="foot-links">
    <span style="left:434px">Our Services</span>
    <span style="left:504px">|</span>
    <span style="left:537px">Subscribe</span>
    <span style="left:602px">|</span>
    <span style="left:630px">Testimonials</span>
    <span style="left:704px">|</span>
    <span style="left:733px">Get in touch</span>
  </div>
  <div class="copyright">Copyright 2016 Fernwick | All rights reserved</div>
  <span class="social" style="left:918px"></span>
  <span class="social" style="left:935px"></span>
  <span class="social" style="left:953px"></span>
</footer>

</body>
</html>
```